Website redesign

We need a bold revamp of our website (http://www.brantocksparkworks.co.nz/)
which at the moment looks dated. We want a crisp, fresh and bold look. The background image behind web page can go. Open to complete new layout

Target Market(s)

Electrical contracting company- working in the domestic and commercial field

Coding

Coded - Design and coding required

Number of Pages Required

5+ page

Font styles to use
Sans Serif

Colors

Designer to choose colors to be used in the design.

```html
<!DOCTYPE html>
<html lang="en">
<head>
<meta charset="utf-8">
<title>Brantock Sparkworks</title>
<link rel="stylesheet" href="https://fonts.googleapis.com/css2?family=Poppins:wght@300;400;500;600&family=Roboto+Condensed:wght@400;700&display=swap">
<style>
:root{
  --red:#d0101b;
  --red-deep:#a8121b;
  --ink:#111111;
  --text:#333333;
  --muted:#555555;
  --white:#ffffff;
  --line:#dddddd;
  --footer:#0b0b0b;
}
*{margin:0;padding:0;box-sizing:border-box}
html,body{width:1200px;height:3377px;overflow:hidden;background:var(--white)}
body{position:relative;font-family:"Poppins",sans-serif;color:var(--text)}
.abs{position:absolute}

/* header */
.site-header{position:absolute;left:0;top:0;width:1200px;height:148px;background:var(--white)}
.brand{left:97px;top:30px;display:flex;align-items:center;gap:10px}
.brand-mark{width:22px;height:22px;background:var(--red)}
.brand-name{font-family:"Roboto Condensed",sans-serif;font-weight:700;font-size:34px;color:var(--ink);line-height:1}
.search{left:597px;top:43px;width:207px;height:40px;border:1px solid #999;border-radius:6px;font-size:13px;color:#888;padding:10px 14px}
.search svg{position:absolute;right:12px;top:11px}
.phone-block{left:830px;top:38px;display:flex;align-items:center;gap:12px}
.phone-block .label{font-size:14px;color:var(--text);line-height:1.2}
.phone-block .num{font-size:18px;color:var(--ink);font-weight:500}
.local-badge{left:1025px;top:16px;width:85px;height:85px;border-radius:50%;background:#5aa84a}

.main-nav{position:absolute;left:88px;top:119px;width:1024px;height:54px;display:flex;z-index:3}
.main-nav a{flex:1;display:flex;align-items:center;justify-content:center;background:var(--red);color:var(--white);text-decoration:none;font-size:17px}
.main-nav a.active{background:var(--ink);flex:0 0 167px}

/* hero */
.hero{position:absolute;left:0;top:148px;width:1200px;height:577px;overflow:hidden}
.hero-photo{position:absolute;inset:0;background:linear-gradient(120deg,#1b2535 0%,#3b4a63 45%,#25303f 70%,#131a24 100%)}
.hero-shapes{position:absolute;left:0;top:0}
.hero-title{left:113px;top:290px;font-family:"Roboto Condensed",sans-serif;font-weight:700;font-size:64px;color:var(--white);line-height:1}
.hero-sub{left:113px;top:370px;font-family:"Roboto Condensed",sans-serif;font-size:25px;color:var(--white)}
.slider-dots{left:1173px;top:248px;display:flex;flex-direction:column;gap:17px}
.slider-dots span{width:9px;height:9px;border-radius:50%;background:var(--white)}

/* section headings */
.section-title{position:absolute;left:0;width:1200px;text-align:center;font-size:34px;font-weight:400;color:var(--ink)}
.section-lead{position:absolute;left:200px;width:800px;text-align:center;font-size:14.5px;line-height:30px;color:var(--muted)}

/* services */
.service-card{position:absolute;width:202px;height:171px;background:var(--white);border-radius:6px;box-shadow:0 2px 10px rgba(0,0,0,.22);display:flex;flex-direction:column;align-items:center;justify-content:center;gap:18px;color:var(--red)}
.service-card span{font-size:16px;color:var(--text)}
.service-card.is-active{background:var(--red);color:var(--white)}
.service-card.is-active span{color:var(--white)}

/* about */
.tools-photo{position:absolute;left:0;top:1463px;width:1200px;height:200px;background:linear-gradient(180deg,#ffffff 0%,#f2e2e2 60%,#e9c9c9 100%)}
.about{position:absolute;left:0;top:1659px;width:1200px;height:516px;background:linear-gradient(90deg,#b40f1a 0%,var(--red) 45%,#b20e18 100%)}
.about-frame{left:131px;top:97px;width:313px;height:304px;border:6px solid var(--white)}
.about-photo{left:164px;top:129px;width:318px;height:304px;background:linear-gradient(135deg,#4a5663,#8b8f88 50%,#3b3f45)}
.about-copy{left:522px;top:140px;width:560px;color:var(--white)}
.about-copy h2{font-size:36px;font-weight:400;margin-bottom:14px}
.about-copy p{font-size:14.5px;line-height:30px;margin-bottom:14px}
.about-copy li{list-style:none;display:flex;align-items:center;gap:14px;font-size:16px;margin-bottom:14px}
.about-copy li.phone{font-size:19px}

/* projects */
.project{position:absolute;width:297px;text-align:center}
.project-photo{width:297px;height:239px;border:7px solid var(--white);box-shadow:0 2px 10px rgba(0,0,0,.25)}
.project h3{font-size:16px;font-weight:400;color:var(--ink);margin-top:26px}
.project p{font-size:13px;color:var(--text);margin-top:8px}
.project a{display:inline-block;margin-top:12px;width:131px;height:32px;line-height:32px;background:var(--red);color:var(--white);border-radius:5px;font-size:14px;text-decoration:none}

/* partners + footer */
.site-footer{position:absolute;left:0;top:2976px;width:1200px;height:401px;background:var(--footer);color:var(--white)}
.partners{position:absolute;left:88px;top:2918px;width:1024px;height:99px;background:var(--white);box-shadow:0 2px 10px rgba(0,0,0,.2);z-index:2;display:flex;align-items:center;justify-content:space-around;padding:0 40px}
.partner-badge{width:150px;height:46px;background:#d6d6d6;border-radius:4px}
.footer-col{position:absolute;top:115px}
.footer-col h4{font-size:15px;font-weight:400;letter-spacing:.5px;margin-bottom:22px}
.footer-col li{list-style:none;font-size:13px;margin-bottom:9px}
.footer-col .contact-row{display:flex;align-items:center;gap:14px;margin-bottom:14px;font-size:13px}
.footer-note{left:835px;top:147px;width:230px;font-size:13px;line-height:20px}
.email-field{left:835px;top:212px;width:219px;height:43px;border:1px solid var(--white);border-radius:22px;font-size:13px;color:#aaa;padding:12px 22px}
.email-field svg{position:absolute;right:14px;top:12px}
.footer-rule{left:83px;top:307px;width:1032px;height:1px;background:#444}
.copyright{left:0;top:340px;width:1200px;text-align:center;font-size:13px}
</style>
</head>
<body>

<header class="site-header">
  <div class="abs brand"><span class="brand-mark"></span><span class="brand-name">Brantock Sparkworks</span></div>
  <div class="abs search">Search
    <svg width="16" height="16" viewBox="0 0 16 16" fill="none" stroke="#333" stroke-width="2"><circle cx="7" cy="7" r="5"/><path d="M11 11l4 4"/></svg>
  </div>
  <div class="abs phone-block">
    <svg width="30" height="30" viewBox="0 0 24 24" fill="var(--red)"><path d="M6.6 10.8a15 15 0 0 0 6.6 6.6l2.2-2.2c.3-.3.7-.4 1-.2 1.1.4 2.3.6 3.6.6.6 0 1 .4 1 1V20c0 .6-.4 1-1 1C10.6 21 3 13.4 3 4c0-.6.4-1 1-1h3.5c.6 0 1 .4 1 1 0 1.3.2 2.5.6 3.6.1.3 0 .7-.2 1z"/></svg>
    <div><div class="label">Free Phone</div><div class="num">0800 55 41 27</div></div>
  </div>
  <div class="abs local-badge" role="img" aria-label="Local business badge"></div>
</header>

<nav class="main-nav">
  <a class="active" href="#">Home</a><a href="#">About Us</a><a href="#">Services</a><a href="#">Projects</a><a href="#">Contact Us</a><a href="#">Info</a>
</nav>

<section class="hero">
  <div class="hero-photo" role="img" aria-label="Electrician in hard hat and gloves holding sparking cables in a workshop"></div>
  <svg class="hero-shapes" width="1200" height="577" viewBox="0 0 1200 577">
    <polygon points="0,480 560,432 1200,520 1200,577 0,577" fill="#c01624" opacity=".55"/>
    <polygon points="0,490 230,577 0,577" fill="var(--red)"/>
    <polygon points="430,577 900,455 1200,560 1200,577" fill="var(--red)" opacity=".8"/>
    <polygon points="200,577 560,440 820,577" fill="#e03a44" opacity=".5"/>
  </svg>
  <div class="abs hero-title">Brantock Sparkworks</div>
  <div class="abs hero-sub">Electrical installation and maintenance</div>
  <div class="abs slider-dots"><span></span><span></span><span></span><span></span></div>
</section>

<h2 class="section-title" style="top:826px">Our Services</h2>
<p class="section-lead" style="top:882px">It is a long established fact that a reader will be distracted by the readable content of a page when looking at its layout. The point of using Lorem Ipsum is that it has a more-or-less normal distribution of letters,</p>

<div class="service-card" style="left:158px;top:995px">
  <svg width="54" height="54" viewBox="0 0 54 54" fill="none" stroke="currentColor" stroke-width="2.5"><circle cx="27" cy="27" r="22"/><rect x="20" y="20" width="14" height="12" rx="3"/><path d="M23 20v-6M31 20v-6M27 32v10"/></svg>
  <span>Electrical</span></div>
<div class="service-card is-active" style="left:387px;top:995px">
  <svg width="76" height="54" viewBox="0 0 76 54" fill="none" stroke="currentColor" stroke-width="2.5"><rect x="3" y="4" width="70" height="24" rx="2"/><path d="M10 20h56M26 36c-3 4 3 6 0 12M38 36c-3 4 3 6 0 12M50 36c-3 4 3 6 0 12"/></svg>
  <span>Appliance</span></div>
<div class="service-card" style="left:610px;top:995px">
  <svg width="50" height="60" viewBox="0 0 50 60" fill="none" stroke="currentColor" stroke-width="2.5"><rect x="3" y="3" width="44" height="54" rx="2"/><path d="M3 16h44"/><rect x="13" y="26" width="24" height="22"/><circle cx="25" cy="37" r="5"/></svg>
  <span>Alarms</span></div>
<div class="service-card" style="left:840px;top:995px">
  <svg width="70" height="54" viewBox="0 0 70 54" fill="none" stroke="currentColor" stroke-width="2.5"><rect x="14" y="8" width="46" height="18" rx="3" transform="rotate(20 37 17)"/><path d="M30 34l-6 12M6 40h18M6 34v14"/></svg>
  <span>Security Camera</span></div>
<div class="service-card" style="left:158px;top:1193px">
  <svg width="64" height="54" viewBox="0 0 64 54" fill="none" stroke="currentColor" stroke-width="2.5"><path d="M6 8h52M6 46h52M12 8v38M22 8v38M32 8v38M42 8v38M52 8v38M6 50v-4M58 50v-4"/></svg>
  <span>Heat Pump</span></div>
<div class="service-card" style="left:387px;top:1193px">
  <svg width="60" height="54" viewBox="0 0 60 54" fill="none" stroke="currentColor" stroke-width="2.5"><rect x="6" y="4" width="48" height="10" rx="2"/><path d="M14 14l4 16h24l4-16"/><circle cx="30" cy="22" r="3"/><path d="M18 40c8 5 16 5 24 0M12 47c12 7 24 7 36 0"/></svg>
  <span>Fire &amp; Smoke</span></div>
<div class="service-card" style="left:610px;top:1193px">
  <svg width="50" height="60" viewBox="0 0 50 60" fill="none" stroke="currentColor" stroke-width="2.5"><rect x="6" y="4" width="14" height="16" rx="2"/><path d="M13 20v18c0 10 24 10 24 0v-6"/><rect x="30" y="24" width="14" height="10" rx="2"/><path d="M37 34v20"/></svg>
  <span>Phone &amp; Data</span></div>
<div class="service-card" style="left:840px;top:1193px">
  <svg width="54" height="58" viewBox="0 0 54 58" fill="none" stroke="currentColor" stroke-width="2.5"><path d="M10 8a26 26 0 0 0 30 30z"/><path d="M25 23l12-12M37 11l4-4"/><path d="M20 40l-8 14h26l-6-14"/></svg>
  <span>Satellites &amp; Aerials,</span></div>

<div class="tools-photo" role="img" aria-label="Electrician tools: pliers, red cable, insulation tape and screwdriver"></div>

<section class="about">
  <div class="abs about-frame"></div>
  <div class="abs about-photo" role="img" aria-label="Technician testing a switchboard with a multimeter"></div>
  <div class="abs about-copy">
    <h2>About us</h2>
    <p>Brantock Sparkworks is a leading electrical installation and maintenance company based in Wanganui, but servicing all New Zealand. With over 15 professionally qualified and experienced Wanganui electricians, technicians and support staff we are leading the way in providing quality electrical services.</p>
    <ul>
      <li><svg width="18" height="18" viewBox="0 0 18 18"><circle cx="9" cy="9" r="9" fill="#fff"/><path d="M7 5l4 4-4 4" stroke="var(--red)" stroke-width="2" fill="none"/></svg>Proudly serving our local community for over 20 years</li>
      <li><svg width="18" height="18" viewBox="0 0 18 18"><circle cx="9" cy="9" r="9" fill="#fff"/><path d="M7 5l4 4-4 4" stroke="var(--red)" stroke-width="2" fill="none"/></svg>Our electrical technicians are on call 24 hour, 7 days a week.</li>
      <li class="phone"><svg width="18" height="18" viewBox="0 0 24 24" fill="#fff"><path d="M6.6 10.8a15 15 0 0 0 6.6 6.6l2.2-2.2c.3-.3.7-.4 1-.2 1.1.4 2.3.6 3.6.6.6 0 1 .4 1 1V20c0 .6-.4 1-1 1C10.6 21 3 13.4 3 4c0-.6.4-1 1-1h3.5c.6 0 1 .4 1 1 0 1.3.2 2.5.6 3.6.1.3 0 .7-.2 1z"/></svg>Phone. 0800 55 41 27 or (06) 421 7390</li>
    </ul>
  </div>
</section>

<h2 class="section-title" style="top:2290px">Our Projects</h2>
<p class="section-lead" style="top:2352px;left:150px;width:900px">It is a long established fact that a reader will be distracted by the readable content of a page when looking at its layout. The point of using Lorem Ipsum is that it has a more-or-less normal distribution of letters,</p>

<div class="project" style="left:99px;top:2449px">
  <div class="project-photo" role="img" aria-label="Retail store front after commercial refit" style="background:linear-gradient(180deg,#c8cdd6 0%,#2d5aa8 30%,#b3131d 55%,#5b4a40 100%)"></div>
  <h3>Denim Loft - Commercial Refit</h3><p>Complete overhaul of retail interior lighting</p><a href="#">View Details</a></div>
<div class="project" style="left:446px;top:2449px">
  <div class="project-photo" role="img" aria-label="Car dealership building with cars parked in front" style="background:linear-gradient(180deg,#aab8c4 0%,#e4e4e4 35%,#8c8c8c 70%,#5d6166 100%)"></div>
  <h3>Riverside Motors - Revamp</h3><p>Complete overhaul of retail interior lighting</p><a href="#">View Details</a></div>
<div class="project" style="left:790px;top:2449px">
  <div class="project-photo" role="img" aria-label="Bank branch building on a street corner" style="background:linear-gradient(180deg,#dfe6ec 0%,#c3ccd4 45%,#6f8090 75%,#8a8f94 100%)"></div>
  <h3>Harbour Bank - Re-modeling</h3><p>Complete overhaul of retail interior lighting</p><a href="#">View Details</a></div>

<div class="partners">
  <div class="partner-badge"></div><div class="partner-badge"></div><div class="partner-badge"></div><div class="partner-badge"></div>
</div>

<footer class="site-footer">
  <div class="footer-col" style="left:131px">
    <h4>INFORMATION</h4>
    <ul><li>» Privacy Policy</li><li>» About Us</li><li>» Projects</li><li>» Contact us</li></ul>
  </div>
  <div class="footer-col" style="left:428px">
    <h4>CONTACT US</h4>
    <div class="contact-row"><svg width="20" height="20" viewBox="0 0 20 20"><circle cx="10" cy="10" r="9" fill="none" stroke="#fff" stroke-width="1.5"/><path d="M10 5a3 3 0 0 0-3 3c0 2.5 3 6 3 6s3-3.5 3-6a3 3 0 0 0-3-3z" fill="#fff"/></svg>14 Kowhai Lane, Wanganui 4500</div>
    <div class="contact-row"><svg width="20" height="20" viewBox="0 0 20 20"><circle cx="10" cy="10" r="9" fill="none" stroke="#fff" stroke-width="1.5"/><path d="M7 6l2 2-1 1.5a6 6 0 0 0 2.5 2.5L12 11l2 2-1.5 1.5C9 14 6 11 5.5 7.5z" fill="#fff"/></svg>0800 55 41 27 or (06) 421 7390</div>
    <div class="contact-row"><svg width="20" height="20" viewBox="0 0 20 20"><circle cx="10" cy="10" r="9" fill="none" stroke="#fff" stroke-width="1.5"/><rect x="5.5" y="7" width="9" height="6" fill="#fff"/><path d="M5.5 7l4.5 3.5L14.5 7" stroke="#0b0b0b" fill="none"/></svg>office@brantocksparkworks.co.nz</div>
  </div>
  <p class="abs footer-note">Your about us information would fit here nicely.</p>
  <div class="abs email-field">Email address
    <svg width="18" height="18" viewBox="0 0 18 18"><circle cx="9" cy="9" r="9" fill="#fff"/><path d="M9 5v8M5 9h8" stroke="#0b0b0b" stroke-width="2"/></svg>
  </div>
  <div class="abs footer-rule"></div>
  <p class="abs copyright">Copyright © 2018. All Rights Reserved</p>
</footer>

</body>
</html>
```